https://www.lernwinkel.de - a website for school website in germany for presentation/paper download

we own the webpage https://www.lernwinkel.de and we need a new webdesign (a new website logo is also possible). we want only new images and css, we don´t want to made any change to the HTML code.
we need only new images/color for a new modern look.

we want to have more trust to our user. they have to download presentation/paper
we need template for this sites:
https://www.lernwinkel.de/
https://www.lernwinkel.de/referate/englisch
https://www.lernwinkel.de/forum.php
https://www.lernwinkel.de/forum/insektenhotel/258614
https://www.lernwinkel.de/referat/latein/sokrates/25892
https://www.lernwinkel.de/schule_seminararbeit_fachliste.php?fach=238
and other sites on the website. (take a look around the website)

we don´t like white color for sublines or text. (h1/h2/strong) . in image are white Text OK.

important: we want to chance ONLY the CSS and PICS, we don´t want to remove or chance any HTML code.

after you have made a mockup of the new design and we give you a go, you have to made a package with the IMAGES and the CSS rules (text how we have to chance the current css)

Target Market(s)

Germany, Austria, Switzerland -DACH

Industry/Entity Type

School

Coding

Coded - Design and coding required

Number of Pages Required

5+ page

Font styles to use
Serif
Sans Serif

Colors

Designer to choose colors to be used in the design.

Requirements
Must have
• We want only to remove images and no HTML Code
Should not have
• NO white colors for Text on the site. In images are OK

```html
<!DOCTYPE html>
<html lang="de">
<head>
<meta charset="utf-8">
<title>Lernwinkel.de – Startseite</title>
<link href="https://fonts.googleapis.com/css2?family=Roboto+Slab:wght@400;700&family=Montserrat:wght@400;600;700&family=Roboto:wght@400;500;700&display=swap" rel="stylesheet">
<style>
:root{
  --yellow:#fbbf3a;
  --dark:#23262b;
  --ink:#1e2126;
  --muted:#8a8f96;
  --line:#dde1e5;
  --soft:#f1f5f8;
  --white:#ffffff;
  --red:#ef5350;
  --green:#8bc34a;
  --blue:#5aa6e0;
  --teal:#4fd6cf;
}
*{box-sizing:border-box;margin:0;padding:0}
html,body{width:1200px;height:2350px;overflow:hidden}
body{position:relative;background:var(--white);font-family:"Roboto",Arial,sans-serif;color:var(--ink)}
.abs{position:absolute}

/* top bar */
.topbar{left:0;top:0;width:1200px;height:53px;background:var(--dark);font-size:10px;color:#8a8f96}
.topbar .hours{left:80px;top:21px}
.topbar .sep{left:226px;top:12px;width:1px;height:30px;background:#3a3e45}
.topbar .socials{left:270px;top:22px;display:flex;gap:24px}
.topbar .socials span{width:8px;height:8px;border-radius:50%;background:#8a8f96;display:block}
.topbar .account{left:1007px;top:20px}

/* header */
.header{left:0;top:53px;width:1200px;height:143px;background:var(--white)}
.brand{left:80px;top:94px;font-family:"Montserrat",sans-serif;font-weight:700;font-size:19px;color:var(--ink);display:flex;align-items:center;gap:8px}
.brand i{width:14px;height:14px;background:var(--yellow);display:block}
.nav{left:265px;top:116px;display:flex;gap:0;font-size:11.5px;font-weight:500;font-family:"Roboto",sans-serif}
.nav span{margin-right:46px;color:var(--ink)}
.nav span::after{content:"";display:inline-block;width:4px;height:4px;border-right:1.3px solid currentColor;border-bottom:1.3px solid currentColor;transform:rotate(45deg);margin-left:7px;vertical-align:3px}
.nav .active{color:var(--yellow)}
.header .vline{left:1004px;top:108px;width:1px;height:34px;background:var(--line)}
.search-ic{left:1047px;top:113px}

/* hero */
.hero{left:0;top:196px;width:1200px;height:529px;background:linear-gradient(100deg,#6f7a6a 0%,#a8b59a 25%,#5b7d9c 50%,#3d5d82 70%,#8aa067 100%)}
.hero-shade{left:0;top:196px;width:1200px;height:529px;background:linear-gradient(90deg,rgba(20,25,30,.35),rgba(20,25,30,0) 60%)}
.hero-title{left:44px;top:300px;font-family:"Roboto Slab",serif;font-weight:700;font-size:66px;color:var(--white);letter-spacing:1px}
.hero-name{left:183px;top:560px;font-family:"Montserrat",sans-serif;font-weight:700;font-size:36px;color:var(--white);display:flex;align-items:center;gap:14px}
.hero-name i{width:22px;height:22px;background:var(--yellow);display:block}
.slide-arrow{top:402px;width:55px;height:90px;background:rgba(60,60,60,.45)}
.slide-arrow.prev{left:0}.slide-arrow.next{left:1150px}
.dots{left:540px;top:692px;display:flex;gap:10px}
.dots span{width:16px;height:16px;background:rgba(255,255,255,.45);display:block}
.dots .on{background:transparent;border:2px solid var(--white)}

/* intro */
.intro{left:0;top:725px;width:1200px;height:705px;background:var(--soft)}
.searchbox{left:80px;top:815px;width:1040px;height:106px;background:var(--white);box-shadow:0 1px 4px rgba(0,0,0,.06)}
.select{left:124px;top:846px;width:285px;height:44px;border:1px solid var(--line);font-size:12px;padding:13px 27px;color:var(--ink)}
.select::after{content:"";position:absolute;right:20px;top:14px;width:7px;height:7px;border-right:2px solid var(--ink);border-bottom:2px solid var(--ink);transform:rotate(45deg)}
.query{left:437px;top:846px;width:329px;height:44px;border:1px solid var(--line);font-size:11.5px;padding:14px 22px;color:var(--ink)}
.searchbox-sep{left:831px;top:846px;width:1px;height:44px;background:var(--line)}
.btn-search{left:962px;top:845px;width:110px;height:44px;background:var(--yellow);color:var(--white);font-family:"Montserrat",sans-serif;font-weight:700;font-size:10px;letter-spacing:1.5px;text-align:center;line-height:44px;box-shadow:4px 4px 0 -1px var(--white),4px 4px 0 0 var(--yellow)}
.greet{left:0;top:985px;width:1200px;text-align:center;font-family:"Roboto Slab",serif;font-size:26px;line-height:32px;color:var(--ink)}
.greet .hl{color:var(--yellow)}
.greet .l1{text-transform:uppercase}
.lead{left:0;top:1058px;width:1200px;text-align:center;font-size:14.5px;line-height:27px;color:var(--muted)}
.feature{top:1202px;width:260px;text-align:center}
.feature .ic{width:62px;height:62px;border-radius:50%;margin:0 auto;display:flex;align-items:center;justify-content:center}
.feature h3{margin-top:34px;font-size:15px;font-weight:700;color:var(--ink);letter-spacing:.3px}
.feature p{margin-top:14px;font-size:13px;line-height:23px;color:#6b7077}
.f1{left:69px}.f2{left:335px}.f3{left:602px}.f4{left:868px}
.f2 .ic{box-shadow:0 5px 10px rgba(0,0,0,.2)}

/* registration */
.rule{left:0;top:1430px;width:1200px;height:8px;background:var(--yellow)}
.card{left:78px;top:1437px;width:419px;height:533px;background:var(--white);box-shadow:0 10px 24px rgba(0,0,0,.12)}
.card-head{left:78px;top:1437px}
.card-title{left:78px;top:1494px;width:419px;text-align:center;font-family:"Montserrat",sans-serif;font-weight:700;font-size:23px;color:var(--white);letter-spacing:.5px}
.field{left:141px;width:292px;height:30px;border-bottom:1px solid var(--line);font-size:13.5px;color:var(--ink)}
.fd1{top:1658px}.fd2{top:1720px}.fd3{top:1786px}
.btn-send{left:190px;top:1868px;width:170px;height:44px;border:2px solid var(--ink);font-family:"Montserrat",sans-serif;font-weight:700;font-size:10px;letter-spacing:2px;text-align:center;line-height:40px;color:var(--ink);box-shadow:5px 5px 0 -2px var(--white),5px 5px 0 0 var(--yellow)}
.reg-kicker{left:589px;top:1545px;font-family:"Montserrat",sans-serif;font-size:34px;letter-spacing:1px;color:var(--ink)}
.reg-title{left:589px;top:1598px;font-family:"Roboto Slab",serif;font-weight:700;font-size:52px;color:var(--yellow);letter-spacing:.5px}
.reg-text{left:589px;top:1688px;width:560px;font-family:"Montserrat",sans-serif;font-size:16px;line-height:22px;color:var(--ink)}
.online{left:712px;top:1870px;display:flex;align-items:baseline;gap:12px;font-family:"Montserrat",sans-serif;color:var(--ink)}
.online b{font-size:60px;font-weight:700}
.online span{font-size:18px;font-weight:600}

/* footer */
.footer{left:0;top:2057px;width:1200px;height:293px;background:var(--dark)}
.f-brand{left:270px;top:2210px;font-family:"Montserrat",sans-serif;font-weight:700;font-size:18px;color:var(--white);display:flex;align-items:center;gap:8px}
.f-brand i{width:12px;height:12px;background:var(--yellow);display:block}
.f-socials{left:283px;top:2270px;display:flex;gap:27px}
.f-socials span{width:8px;height:8px;border-radius:50%;background:#a7acb3;display:block}
.f-sep{left:600px;top:2150px;width:1px;height:150px;background:#3a3e45}
.contact{left:712px;top:2178px;font-family:"Montserrat",sans-serif;font-size:13.5px;line-height:33px;color:#a7acb3}
.contact b{color:var(--yellow);font-weight:700}
.totop{left:1149px;top:2303px}
</style>
</head>
<body>

<div class="abs topbar">
  <div class="abs hours">Mon - Fri: 8.00 - 18:00</div>
  <div class="abs sep"></div>
  <div class="abs socials"><span></span><span></span><span></span><span></span></div>
  <div class="abs account">Login &nbsp;&nbsp;|&nbsp;&nbsp; Registrieren</div>
</div>

<div class="abs header"></div>
<div class="abs brand"><i></i>LERNWINKEL.DE</div>
<nav class="abs nav">
  <span class="active">STARTSEITE</span><span>FOREN</span><span>Mitglieder</span><span>Flirtsuche</span><span>Informationen</span><span>LiveMessenger</span>
</nav>
<div class="abs vline"></div>
<svg class="abs search-ic" width="26" height="26" viewBox="0 0 26 26" fill="none" stroke="#1e2126" stroke-width="1.6"><circle cx="10.5" cy="10.5" r="8"/><line x1="16.5" y1="16.5" x2="24" y2="24"/></svg>

<div class="abs hero" role="img" aria-label="Foto: lachende Schülergruppe schaut gemeinsam auf einen Laptop, im Hintergrund ein Schulgebäude mit Bäumen"></div>
<div class="abs hero-shade"></div>
<div class="abs hero-title">WILLKOMMEN ZU</div>
<div class="abs hero-name"><i></i>LERNWINKEL.DE</div>
<div class="abs slide-arrow prev"><svg width="55" height="90" viewBox="0 0 55 90" fill="none" stroke="#fff" stroke-width="2"><polyline points="32,28 18,45 32,62"/></svg></div>
<div class="abs slide-arrow next"><svg width="55" height="90" viewBox="0 0 55 90" fill="none" stroke="#fff" stroke-width="2"><polyline points="23,28 37,45 23,62"/></svg></div>
<div class="abs dots"><span></span><span></span><span></span><span></span><span class="on"></span></div>

<section class="abs intro"></section>
<div class="abs searchbox"></div>
<div class="abs select">Suchbegriff</div>
<div class="abs query">Was suchst du? Hier eingeben!</div>
<div class="abs searchbox-sep"></div>
<div class="abs btn-search">SUCHEN</div>

<h1 class="abs greet"><span class="l1">Hallo <span class="hl">Besucher,</span></span><br>Es sind bereits <span class="hl">401324</span> Mitglieder bei uns registriert!</h1>
<p class="abs lead">Auf Lernwinkel.de findest du viele Referate, Facharbeiten und Hausaufgaben.<br>Solltest du einmal ein Referat zu einem Thema nicht finden,<br>kannst du deine Frage bei uns im Forum stellen, wo dir in der Regel schnell geholfen wird.</p>

<div class="abs feature f1">
  <div class="ic" style="background:var(--red)"><svg width="26" height="26" viewBox="0 0 26 26" fill="none" stroke="#fff" stroke-width="1.6"><circle cx="13" cy="13" r="9"/><path d="M8 11c2 0 3 2 5 1s2-4 4-3M9 17c2-1 4 0 5 2"/></svg></div>
  <h3>REFERATE - HAUSARBEITEN</h3>
  <p>The Hausaufgaben zu folgenden<br>Fächern</p>
</div>
<div class="abs feature f2">
  <div class="ic" style="background:var(--green)"><svg width="28" height="26" viewBox="0 0 28 26" fill="none" stroke="#fff" stroke-width="1.6"><circle cx="8" cy="8" r="2.5"/><circle cx="20" cy="8" r="2.5"/><circle cx="14" cy="10" r="2.5"/><path d="M5 20v-6h6v6M17 20v-6h6v6M11 22v-7h6v7"/></svg></div>
  <h3>FOREN</h3>
  <p>Foren</p>
</div>
<div class="abs feature f3">
  <div class="ic" style="background:var(--blue)"><svg width="26" height="26" viewBox="0 0 26 26" fill="none" stroke="#fff" stroke-width="1.6"><circle cx="10" cy="10" r="5.5"/><circle cx="16" cy="16" r="5.5"/></svg></div>
  <h3>LIVEMESSENGER</h3>
  <p>Diese Funktion ist nur für Mitglieder<br>verfügbar.</p>
</div>
<div class="abs feature f4">
  <div class="ic" style="background:var(--teal)"><svg width="26" height="26" viewBox="0 0 26 26" fill="none" stroke="#fff" stroke-width="1.6"><rect x="4" y="8" width="18" height="13"/><path d="M10 8V5h6v3M4 13h18"/></svg></div>
  <h3>SCHULE &amp; UNI</h3>
  <p>Willkommen im Schule und Uni-<br>Bereich von Lernwinkel.de.</p>
</div>

<div class="abs rule"></div>
<div class="abs card"></div>
<svg class="abs card-head" width="419" height="170" viewBox="0 0 419 170"><polygon points="0,0 419,0 419,136 209.5,170 0,136" fill="#fbbf3a"/></svg>
<h2 class="abs card-title">PERSÖNLICHE ANGABEN</h2>
<div class="abs field fd1">Nickname:</div>
<div class="abs field fd2">Email *:</div>
<div class="abs field fd3">Vorname:</div>
<div class="abs btn-send">ABSENDEN</div>

<div class="abs reg-kicker">ANMELDUNG</div>
<h2 class="abs reg-title">JETZT REGISTRIERE</h2>
<p class="abs reg-text">Hier kannst du dich kostenlos bei Lernwinkel.de anmelden. Bitte fülle alle Felder mit richtigen Angaben aus, damit deine Anmeldung angenommen wird. Mitglieder deren Angaben falsch sind, werden bei Lernwinkel.de nicht akzeptiert. Es entstehen mit dieser Anmeldung keinerlei Kosten. Nach der Anmeldung erhältst du eine E-Mail, in der du deine Registrierung bei uns bestätigen musst.</p>
<div class="abs online"><b>204</b><span>Mitglieder online</span></div>

<footer class="abs footer"></footer>
<div class="abs f-brand"><i></i>LERNWINKEL.DE</div>
<div class="abs f-socials"><span></span><span></span><span></span><span></span></div>
<div class="abs f-sep"></div>
<div class="abs contact"><b>P:</b> 00-00-000-000<br><b>E:</b> kontakt@lernwinkel.de<br><b>A:</b> Lorem Ipsum</div>
<svg class="abs totop" width="26" height="26" viewBox="0 0 26 26" fill="none" stroke="#fbbf3a" stroke-width="1.5"><circle cx="13" cy="13" r="11.5"/><polyline points="8,15 13,10 18,15"/></svg>

</body>
</html>
```